Wordpress Design Project

We are a local restaurant who needs a quality online identity base. We operate in a 1930's Villa, and our target market is the below mid - upper. Our main sale is the evening dinner meal, while we also sell home-made goods, including preserves, and handmade chocolates.
The final Wordpress coded design will:
Be a base for information including Contact details, and a Map of it's location. It will also include photographs of some of the dishes to give an idea to potential customers as to the style and target market.
The site will have 4 main pages
-Main
-About
-Menu
-Contact
Ideas for elements we would like to have included in the design are
Cardboard tags with the links to the other pages, which give a home-made feel
Character wood, with deep grain to emphasis our homely feel
An 'aged' map of the location. Possibly on a large cardboard tag.
Link to our Facebook page
Link to our Plate Finder review page http://www.platefinder.co.nz/restaurant.php?rest=4720
Notes:
The final Wordpress site should communicate a homely inviting image, with deep character, while still looking elegant and slightly simplistic. We would like fine fonts, with nice spacing, especially on the cardboard tags.
I have attached a mockup of our very loose vision for the site to give you an idea of the line we would like to go down. This is just for initial ideas, and we are happy for radically different designs, or just neat variations on the base design
Professional, edited photos of the food available will be uploaded alongside this project
Villa Marrow does not have an official Logo for use on the website, so a simple header that ties in with the page will be fine. This may be replaced eventually with a new logo
Address and Hosting is already setup with the address being www.villamarrowkitchen.co.nz with a placeholder site online.
We look forward to all designs, and welcome any questions. This should be an nice job for someone with an eye for detail.

```html
<!DOCTYPE html>
<html lang="en">
<head>
<meta charset="utf-8">
<title>Villa Marrow — Home</title>
<link rel="stylesheet" href="https://fonts.googleapis.com/css2?family=Handlee&family=Arimo:wght@700&family=PT+Sans&display=swap">
<style>
  :root {
    --wood-dark: #2a0805;
    --wood-mid: #5a1a10;
    --wood-light: #6e2416;
    --panel: #414141;
    --bar-top: #555555;
    --bar-bottom: #0e0e0e;
    --accent: #e8423f;
    --accent-soft: #f07a78;
    --white: #ffffff;
    --photo-warm: #5b3415;
    --photo-deep: #140a04;
  }
  * { box-sizing: border-box; margin: 0; padding: 0; }
  html, body { width: 1200px; height: 816px; overflow: hidden; }
  body {
    position: relative;
    background:
      repeating-linear-gradient(90deg, rgba(0,0,0,0.12) 0 3px, transparent 3px 17px, rgba(255,255,255,0.03) 17px 19px, transparent 19px 41px),
      linear-gradient(90deg, var(--wood-dark), var(--wood-mid) 30%, var(--wood-light) 55%, var(--wood-mid) 80%, var(--wood-dark));
    font-family: "Handlee", cursive;
    color: var(--white);
  }
  .page-panel {
    position: absolute; left: 88px; top: 45px; width: 1024px; height: 669px;
    background: var(--panel); border-radius: 6px;
  }
  .main-nav {
    position: absolute; left: 88px; top: 45px; width: 1024px; height: 63px;
    background: linear-gradient(var(--bar-top), var(--bar-bottom));
    border-radius: 6px 6px 0 0;
  }
  .nav-link {
    position: absolute; top: 10px; font-size: 32px; line-height: 40px;
    color: var(--white); text-decoration: none; transform: translateX(-50%);
  }
  .nav-link.is-current::after {
    content: ""; position: absolute; left: 0; right: 0; top: 40px; height: 4px; background: var(--accent);
  }
  .site-name {
    position: absolute; left: 600px; top: 58px; transform: translateX(-50%);
    font-size: 40px; line-height: 44px; color: var(--white); white-space: nowrap;
  }
  .contact-info {
    position: absolute; right: 110px; top: 121px; text-align: right;
    font-size: 18px; line-height: 25px;
  }
  .contact-info .label { color: var(--accent-soft); }
  .hero {
    position: absolute; left: 110px; top: 188px; width: 700px; height: 305px;
    background: var(--white); padding: 7px 6px 6px 6px;
  }
  .hero-photo {
    width: 100%; height: 100%;
    background: radial-gradient(ellipse at 55% 55%, #b89a72 0%, var(--photo-warm) 35%, var(--photo-deep) 80%);
  }
  .testimonials {
    position: absolute; left: 827px; top: 188px; width: 265px; height: 305px;
    background: var(--accent); padding: 16px 20px 0 22px;
  }
  .testimonials h2 { font-weight: 400; font-size: 26px; line-height: 32px; }
  .testimonials blockquote {
    margin-top: 20px; font-family: "Arimo", sans-serif; font-weight: 700;
    font-size: 12.5px; line-height: 18px;
  }
  .testimonials cite {
    display: block; margin-top: 16px; text-align: right; font-style: normal;
    font-family: "Arimo", sans-serif; font-weight: 700; font-size: 14px;
  }
  .gallery-title {
    position: absolute; left: 110px; top: 508px; font-weight: 400; font-size: 26px; line-height: 34px;
  }
  .gallery {
    position: absolute; left: 111px; top: 553px; width: 982px; height: 135px; background: var(--white);
  }
  .gallery-thumb { position: absolute; top: 7px; width: 182px; height: 122px; }
  .thumb-candles { background: linear-gradient(135deg, #3a2a1a, #8a6a3a 55%, #2a1c10); }
  .thumb-goods { background: linear-gradient(135deg, #6a5a3c, #b09a70 50%, #4a3c28); }
  .thumb-wine { background: linear-gradient(135deg, #4a5a8a, #8a7a5a 50%, #3a2a1a); }
  .thumb-lights { background: linear-gradient(135deg, #1a2a3a, #c08a40 55%, #3a2a1a); }
  .gallery-arrow { position: absolute; top: 53px; width: 32px; height: 32px; }
  .location-map {
    position: absolute; left: 94px; top: 726px; width: 145px; height: 73px; border-radius: 6px;
    background: linear-gradient(135deg, #d8d4c4, #c4c8b4 50%, #b8bcb0);
  }
  .copyright {
    position: absolute; right: 99px; top: 735px; font-family: "PT Sans", sans-serif; font-size: 12px;
  }
</style>
</head>
<body>
  <div class="page-panel"></div>

  <nav class="main-nav" aria-label="Main">
    <a class="nav-link is-current" href="#" style="left:93px">home</a>
    <a class="nav-link" href="#" style="left:281px">about</a>
    <a class="nav-link" href="#" style="left:755px">work</a>
    <a class="nav-link" href="#" style="left:932px">contact</a>
  </nav>

  <h1 class="site-name">Villa Marrow</h1>

  <address class="contact-info" style="font-style:normal">
    <div><span class="label">Phone:</span> 03 415 0287</div>
    <div><span class="label">Email:</span> villamarrow08@postbox.co.nz</div>
  </address>

  <div class="hero">
    <div class="hero-photo" role="img" aria-label="Photograph of a plated dessert with berries and cream on a candlelit table"></div>
  </div>

  <section class="testimonials">
    <h2>Testimonials</h2>
    <blockquote>“Lorem Ipsum is simply dummy text of the printing and typesetting industry. Lorem Ipsum has been the industry's standard dummy text ever since the 1500s, when an unknown printer took a galley of type and scrambled it to make a type specimen book. It has survived not only five centuries, but also the leap into electronic typesetting”</blockquote>
    <cite>- Lorem Ipsum</cite>
  </section>

  <h2 class="gallery-title">Photo Gallery</h2>
  <section class="gallery" aria-label="Photo gallery">
    <svg class="gallery-arrow" style="left:11px" viewBox="0 0 32 32" aria-label="Previous">
      <circle cx="16" cy="16" r="15" fill="var(--accent)"/>
      <circle cx="16" cy="16" r="11.5" fill="none" stroke="#fff" stroke-width="1.5"/>
      <path d="M18 10 L12 16 L18 22" fill="none" stroke="#fff" stroke-width="3" stroke-linecap="round" stroke-linejoin="round"/>
    </svg>
    <div class="gallery-thumb thumb-candles" style="left:55px" role="img" aria-label="Photograph of candles along a dining room bench"></div>
    <div class="gallery-thumb thumb-goods" style="left:275px" role="img" aria-label="Photograph of home-made chocolates in paper bags with tags"></div>
    <div class="gallery-thumb thumb-wine" style="left:505px" role="img" aria-label="Photograph of wine bottles in a wooden box beside hydrangeas"></div>
    <div class="gallery-thumb thumb-lights" style="left:738px" role="img" aria-label="Photograph of candle holders glowing on a table"></div>
    <svg class="gallery-arrow" style="left:934px" viewBox="0 0 32 32" aria-label="Next">
      <circle cx="16" cy="16" r="15" fill="var(--accent)"/>
      <circle cx="16" cy="16" r="11.5" fill="none" stroke="#fff" stroke-width="1.5"/>
      <path d="M14 10 L20 16 L14 22" fill="none" stroke="#fff" stroke-width="3" stroke-linecap="round" stroke-linejoin="round"/>
    </svg>
  </section>

  <div class="location-map" role="img" aria-label="Street map showing the restaurant location"></div>

  <p class="copyright">© 2012. All Rights Reserved.</p>
</body>
</html>
```